Squarespace website build: Quill literary annual (initial design work supplied)

Our brand guidelines provide the look and feel for the website - we just need someone to create it based on our mock ups!
PLEASE NOTE:
- Please base our website off the website pages within the brief (ie homepage is GREEN)
- please ensure each page will be standalone (not a scrolling home page)
- please only use filtered duotone style photography as a hold, if you think the page needs a photo.
-please not the websites i have provided as an influence - especially BRINE ANNUAL. We want very little photography.

Quill is a literary and arts journal that provides a platform for both emerging and established writers and artists from New Zealand and beyond. We are passionate about sharing insights into the intimate and unique worlds of creatives with short stories, poetry, and art – showcasing raw and unfiltered glimpses into their world.

We have our brand guidelines and logo finalised, with a 'look and feel' design for the website within our attached brand guidelines document. We just need someone to design this simple website on Squarespace for us. It will have five pages and will need a newsletter sign up link:
Home page
About us page
Submissions page
Purchase page
Contact page

DRAFT WEB COPY

ABOUT
QUILL is an independent literary annual journal established in 2022 by Harriet Calloway and Mereana Platt that publishes unrepentant unfiltered accounts of life, eclectic takes on the mundane ordinary, and deep dives into modern love & sexuality.
Founder, Editor: Harriet Anahera Calloway
Founder, Production Director: Mereana Platt
Art Direction: Corin Ashby
Editorial Assistant: Lucy Fenwick-Dorsey

I suggest duotone fashion-esque photography which is very Marla Quiggin/ Palm Springs vibe but not obviously identifiable.
· I love the style of Rex Havelin for our shoot in particular. Group lazing around a pool, leisurely, glam, but effortless and ironically looking very natural – as though – yes, these are our lives.
SUBMISSION PAGE
Quill welcomes submissions all year round.
We are drawn to dark humour, satirical takes on the social scene, and starkly honest accounts of ordinary life. Diversity is celebrated, adversity is welcomed and, above all, personal expression is championed. We are particularly seeking content that takes risks, screams of honesty and celebrates life’s most extraordinary moments.
Selected works will be published in our annual publication.

Submission guidelines
We accept flash fiction, short stories and poetry. Individual entries not to mustn’t exceed 2000 words.
Submitted work must be unpublished and in English. We welcome simultaneous submissions, but must be notified immediately if your manuscript is accepted for publication elsewhere or appears in any print or online source. We will endeavour to respond to all submissions within four weeks.
Please send submissions as a word document along with a brief bio of 50 words to inkwell@quilljournal.example
PO Box[EB2]
​Note on Copyright: Copyright remains with the author.

Annual short story competition
Issue One is interested in all that is spiritual, coincidental, or mysterious. Stories selected for this issue reflect life’s uncanny moments, those that defy explanation, and experiences that promote personal and spiritual growth. Entires must be no longer than 2000 words.

First prize: 1000
Second prize: 500
Third prize: 200[EB3]

SUPPORT US
Since our launch in 2022, we have relied upon the generous support of our creative business community in Wellington City, New Zealand. If you read us, or love our ethos, please consider a donation.
Link to chipinhere page
Updates

Hello designers
I would ideally love to have someone turn this around within a few weeks, because the design work has mostly been provided.
Thanks
Harriet

Hi everyone Please ensure you read our brand guidelines and follow the brief. Please note we do not yet have a product, as this is a new venture, so there is no point including images of a magazine that doesn't yet exist. Some further comment to ensure we get there: - We want all pages to be separate pages (not a scrolling home page) with a different colour based on the guidelines - The home page must look just as it does in the brand guidelines - There is no archive page (please read brief) as we have no archive yet. The pages are: Home, About, Contact, Competitions and submissions Thank you

Target Market(s)

writers and creatives

Industry/Entity Type

Writing/ creative/ publishing

Coding

Coded - Design and coding required

Number of Pages Required

4 page

Font styles to use
Other font styles liked:
• COTTA and Univers - as per brand guidelines

Requirements
Must have
• Squarespace designer needed to design our mocked up webpages.
Nice to have
• As close to the brand guideline mock ups as possible (see page 11,12,13)
Should not have
• anything outside of the brand guidelines

```html
<!DOCTYPE html>
<html lang="en">
<head>
<meta charset="utf-8">
<title>Quill — Literary Annual</title>
<link href="https://fonts.googleapis.com/css2?family=Italiana&family=Archivo:wght@400;500;600&display=swap" rel="stylesheet">
<style>
:root{
  --green:#63762f;
  --purple:#6b3d66;
  --mustard:#c4a90f;
  --mustard-soft:#d4bd45;
  --rose:#b84d6b;
  --cream:#f3ede1;
  --white:#ffffff;
  --ink:#2b2b2b;
  --muted:#8a8a8a;
  --display:"Italiana", serif;
  --body:"Archivo", sans-serif;
}
*{margin:0;padding:0;box-sizing:border-box}
html,body{width:1200px;height:3416px;overflow:hidden}
body{position:relative;background:var(--white);font-family:var(--body);color:var(--ink)}
.abs{position:absolute}
a{color:inherit;text-decoration:none}

/* Header / hero */
.hero{left:0;top:0;width:1200px;height:872px;background:var(--green)}
.nav-link{top:76px;font-size:13px;font-weight:600;color:var(--white);letter-spacing:.2px}
.home-dot{left:236px;top:76px;width:14px;height:14px}
.brand{left:0;width:1200px;top:22px;text-align:center;font-family:var(--display);font-size:86px;line-height:110px;color:var(--white)}
.cart{left:928px;top:68px}
.cart-count{left:952px;top:63px;font-size:10px;color:var(--white);font-weight:600}
.btn-outline{border:2px solid var(--white);color:var(--white);font-size:13px;font-weight:600;display:flex;align-items:center;justify-content:center}
.nav-subscribe{left:979px;top:62px;width:132px;height:43px}
.hero-title{left:0;width:1200px;top:210px;text-align:center;font-family:var(--display);font-weight:400;font-size:46px;line-height:56px;color:var(--white)}
.hero-title .read{border-bottom:2px solid var(--rose);padding-bottom:2px}
.hero-frame{left:139px;top:438px}
.hero-photo{left:159px;top:451px;width:874px;height:421px;background:linear-gradient(135deg,#c2385d 0%,#b02a4f 45%,#8e1a38 100%)}

/* About */
.about{left:0;top:872px;width:1200px;height:714px;background:var(--purple)}
.cover{width:367px;height:488px;left:160px;top:988px;background:var(--mustard);box-shadow:0 28px 40px rgba(40,15,35,.35)}
.cover-brand{position:absolute;left:0;width:100%;top:22px;text-align:center;font-family:var(--display);font-size:76px;line-height:84px;color:var(--green)}
.cover-tag{position:absolute;top:82px;font-size:13px;color:var(--rose);letter-spacing:.5px}
.cover-frame{position:absolute;left:28px;top:168px;width:311px;height:320px;border:1px solid var(--green);border-bottom:none}
.cover-photo{position:absolute;left:30px;top:170px;width:307px;height:318px;background:linear-gradient(180deg,#5c7a2e,#7c8c27)}
.about-title{left:611px;top:1074px;font-family:var(--display);font-weight:400;color:var(--mustard);white-space:nowrap}
.about-title .small{font-size:50px}
.about-title .big{font-size:110px;line-height:120px}
.about-copy{left:611px;top:1210px;width:400px;font-size:15.5px;line-height:24px;color:var(--white)}
.about-btn{left:613px;top:1354px;width:153px;height:46px;font-weight:500;font-size:15px}

/* Catalogue */
.catalogue-title{left:0;width:1200px;top:1712px;text-align:center;font-family:var(--display);font-weight:400;font-size:47px;line-height:50px;color:var(--purple)}
.issue-card{top:1936px;width:246px;height:301px;background:var(--white);box-shadow:0 18px 30px rgba(0,0,0,.08)}
.issue-cover{top:1870px;width:196px;height:261px}
.issue-cover .mini-brand{position:absolute;left:0;width:100%;top:6px;text-align:center;font-family:var(--display);font-size:44px;line-height:52px}
.issue-cover .mini-photo{position:absolute;left:14px;top:86px;width:168px;height:175px}
.issue-name{top:2164px;width:246px;text-align:center;font-size:16px}
.issue-buy{top:2187px;width:246px;text-align:center;font-size:13px;font-weight:600;color:var(--muted);letter-spacing:.3px}

/* Newsletter */
.badge{left:122px;top:2432px;width:122px;height:122px;border-radius:50%;background:var(--purple)}
.news-title{left:134px;top:2578px;font-family:var(--display);font-weight:400;font-size:49px;line-height:49px;color:var(--purple)}
.news-sub{left:135px;top:2692px;font-size:16px}
.news-input{left:135px;top:2736px;width:224px;height:56px;background:#f4f4f4;color:#9a9a9a;font-size:16px;display:flex;align-items:center;padding-left:29px}
.news-btn{left:359px;top:2736px;width:170px;height:56px;background:var(--rose);color:var(--white);font-size:16px;font-weight:500;display:flex;align-items:center;justify-content:center}
.accent-block{left:565px;top:2791px;width:44px;height:122px;background:var(--mustard-soft)}
.accent-block.base{left:565px;top:2869px;width:122px;height:44px}
.news-photo{left:599px;top:2354px;width:512px;height:528px;background:radial-gradient(ellipse at 55% 45%,#b8c28e 0%,#8a9a58 45%,#6f8140 100%);box-shadow:0 30px 40px rgba(0,0,0,.12)}

/* Footer */
.footer{left:0;top:3029px;width:1200px;height:387px;background:var(--purple)}
.footer-brand{left:135px;top:3140px;font-family:var(--display);font-size:80px;line-height:100px;color:var(--mustard)}
.footer-head{top:3136px;font-size:19px;font-weight:600;color:var(--mustard)}
.footer-link{left:423px;font-size:15px;color:var(--white)}
.footer-mail{left:643px;top:3172px;font-size:15px;color:var(--white);white-space:nowrap}
.social{top:3185px;width:38px;height:38px;border-radius:50%;background:var(--mustard);color:var(--white);font-size:12px;font-weight:600;display:flex;align-items:center;justify-content:center}
.footer-rule{left:89px;top:3364px;width:1022px;height:1px;background:rgba(255,255,255,.3)}
.copyright{left:0;width:1200px;top:3381px;text-align:center;font-size:14.5px;color:var(--white)}
</style>
</head>
<body>

<section class="abs hero" aria-label="Home hero"></section>
<svg class="abs home-dot" viewBox="0 0 14 14" aria-hidden="true"><path d="M1 7 L7 1.5 L13 7 V13 H1 Z" fill="var(--rose)"/></svg>
<a class="abs nav-link" style="left:280px" href="#">ABOUT US</a>
<a class="abs nav-link" style="left:380px" href="#">SUBMISSIONS</a>
<div class="abs brand">Quill</div>
<a class="abs nav-link" style="left:709px" href="#">PURCHASE</a>
<a class="abs nav-link" style="left:811px" href="#">CONTACT</a>
<svg class="abs cart" width="26" height="24" viewBox="0 0 26 24" aria-label="Cart"><path d="M1 3 H5 L8 16 H21 L24 6 H6" fill="none" stroke="#fff" stroke-width="2"/><circle cx="10" cy="20.5" r="2" fill="#fff"/><circle cx="19" cy="20.5" r="2" fill="#fff"/></svg>
<span class="abs cart-count">0</span>
<a class="abs btn-outline nav-subscribe" href="#">SUBSCRIBE</a>

<h1 class="abs hero-title">Quill is a Plucky Little Pubication<br>Out of Wellington, New Zealand–give it a<br><span class="read">Read Here</span></h1>

<svg class="abs hero-frame" width="912" height="434" viewBox="0 0 912 434" aria-hidden="true">
  <path d="M0.5 434 V48 H14 V20 H44 V0.5 H868 V20 H898 V48 H911.5 V434" fill="none" stroke="var(--mustard)" stroke-width="1.2"/>
  <path d="M14 434 V60 H24 V32 H56 V12 H856 V32 H888 V60 H898 V434" fill="none" stroke="var(--mustard)" stroke-width="1"/>
</svg>
<div class="abs hero-photo" role="img" aria-label="Duotone photograph of a red concrete building facade with angled balconies"></div>

<section class="abs about" aria-label="About"></section>
<div class="abs cover" role="img" aria-label="Issue cover mock-up">
  <span class="cover-tag" style="left:34px">ISSUE 001</span>
  <div class="cover-brand">Quill</div>
  <span class="cover-tag" style="right:34px">DEC 2022</span>
  <div class="cover-frame"></div>
  <div class="cover-photo" role="img" aria-label="Duotone portrait photograph of a woman in glasses"></div>
</div>
<h2 class="abs about-title"><span class="small">About </span><span class="big">Quill</span></h2>
<p class="abs about-copy">QUILL is an independent literary annual journal established in 2022 by Harriet Calloway and Mereana Platt that publishes unrepentant unfiltered accounts of life, eclectic takes on the mundane ordinary, and deep dives into modern love &amp; sexuality.</p>
<a class="abs btn-outline about-btn" href="#">READ MORE</a>

<h2 class="abs catalogue-title">Our back catalogue is available<br>in digital format for a reduced price.</h2>

<div class="abs issue-card" style="left:89px"></div>
<div class="abs issue-card" style="left:347px"></div>
<div class="abs issue-card" style="left:607px"></div>
<div class="abs issue-card" style="left:865px"></div>

<div class="abs issue-cover" role="img" aria-label="Issue 001 cover" style="left:114px;background:var(--cream)"><div class="mini-brand" style="color:var(--green)">Quill</div><div class="mini-photo" style="background:linear-gradient(180deg,#b89a14,#c8ac1c)"></div></div>
<div class="abs issue-cover" role="img" aria-label="Issue 002 cover" style="left:375px;background:var(--rose)"><div class="mini-brand" style="color:var(--white)">Quill</div><div class="mini-photo" style="background:linear-gradient(180deg,#5a2f56,#7a4870)"></div></div>
<div class="abs issue-cover" role="img" aria-label="Issue cover for October" style="left:632px;background:var(--cream)"><div class="mini-brand" style="color:var(--rose)">Quill</div><div class="mini-photo" style="background:linear-gradient(180deg,#3f6a2c,#6f8a2e)"></div></div>
<div class="abs issue-cover" role="img" aria-label="Issue cover for November" style="left:888px;background:var(--green)"><div class="mini-brand" style="color:var(--mustard)">Quill</div><div class="mini-photo" style="background:linear-gradient(180deg,#a83a60,#c45a7a)"></div></div>

<div class="abs issue-name" style="left:89px">ISSUE 001 — AUG 2022</div>
<div class="abs issue-buy" style="left:89px">BUY THE BOOK</div>
<div class="abs issue-name" style="left:347px">ISSUE 002 — SEP 2022</div>
<div class="abs issue-buy" style="left:347px">BUY THE BOOK</div>
<div class="abs issue-name" style="left:607px">ISSUE 001 — OCT 2022</div>
<div class="abs issue-buy" style="left:607px">BUY THE BOOK</div>
<div class="abs issue-name" style="left:865px">ISSUE 001 — NOV 2022</div>
<div class="abs issue-buy" style="left:865px">BUY THE BOOK</div>

<div class="abs badge" aria-hidden="true"></div>
<h2 class="abs news-title">Subscribe to our<br>weekly newsletter</h2>
<p class="abs news-sub">Sign up for news and updates.</p>
<div class="abs news-input">Email Address</div>
<a class="abs news-btn" href="#">SUBSCRIBE</a>
<div class="abs accent-block" role="img" aria-label="Mustard decorative accent"></div>
<div class="abs accent-block base" aria-hidden="true"></div>
<div class="abs news-photo" role="img" aria-label="Green duotone portrait photograph of a woman in glasses"></div>

<footer class="abs footer"></footer>
<div class="abs footer-brand">Quill</div>
<div class="abs footer-head" style="left:423px">Useful Links</div>
<a class="abs footer-link" style="top:3174px" href="#">About us</a>
<a class="abs footer-link" style="top:3200px" href="#">Submissions</a>
<a class="abs footer-link" style="top:3227px" href="#">Purchase</a>
<a class="abs footer-link" style="top:3253px" href="#">Contact</a>
<div class="abs footer-head" style="left:643px">Contact Us</div>
<a class="abs footer-mail" href="#">inkwell@quilljournal.example</a>
<a class="abs social" style="left:879px" href="#" aria-label="Chatter">C</a>
<a class="abs social" style="left:924px" href="#" aria-label="Pinboard">P</a>
<a class="abs social" style="left:969px" href="#" aria-label="Snapframe">S</a>
<div class="abs footer-rule"></div>
<p class="abs copyright">©Copyright 2022 | All Rights Reserved</p>

</body>
</html>
```